Simple and clean

We need a business card design for a new company called Dwelling Owl. It is a search engine to find current properties for sale or rent in New Zealand market.
We have already a colour scheme that we would like people to use.
Light brown: #D4CCB0
Light green: #D6E4D4
Green: #669966
Black/White
It is OK to divert from this colour scheme slightly as long as there is a green component to the business card.
Final design should be clean, simple and should communicate the nature of the business.
Target Market(s)
- First home buyers
- Real estate agents
- People seeking rentals
Industry/Entity Type
Business
Requirements
Must have
- Use those or similar colours.
Light brown: #D4CCB0
Light green: #D6E4D4
Green: #669966
Black/White

```html
<!DOCTYPE html>
<html lang="en">
<head>
<meta charset="utf-8">
<title>Dwelling Owl – Business Card</title>
<link rel="stylesheet" href="https://fonts.googleapis.com/css2?family=Arvo:wght@400;700&family=Rokkitt:wght@400;500;600&display=swap">
<style>
  :root {
    --card-green: #7fa98a;
    --band-green: #8fb493;
    --band-overlap: #9bbd9e;
    --ink: #2b3631;
    --logo-white: #ffffff;
  }
  html, body {
    margin: 0;
    padding: 0;
    width: 1200px;
    height: 686px;
    overflow: hidden;
    background: var(--card-green);
  }
  .business-card {
    display: block;
    width: 1200px;
    height: 686px;
  }
  .card-base { fill: var(--card-green); }
  .accent-band { fill: var(--band-green); }
  .accent-overlap { fill: var(--band-overlap); }
  .web-contacts {
    font-family: "Rokkitt", serif;
    font-size: 33px;
    fill: var(--ink);
  }
  .brand-name {
    font-family: "Arvo", serif;
    font-size: 70px;
    fill: var(--logo-white);
  }
  .person-name {
    font-family: "Rokkitt", serif;
    font-weight: 400;
    font-size: 58px;
    fill: var(--ink);
  }
  .person-role {
    font-family: "Rokkitt", serif;
    font-weight: 600;
    font-size: 38px;
    fill: var(--ink);
  }
  .postal-address,
  .phone-numbers {
    font-family: "Rokkitt", serif;
    font-size: 28px;
    fill: var(--ink);
  }
</style>
</head>
<body>
<svg class="business-card" viewBox="0 0 1200 686" width="1200" height="686" xmlns="http://www.w3.org/2000/svg">
  <rect class="card-base" x="0" y="0" width="1200" height="686"/>

  <rect class="accent-band" x="0" y="138" width="697" height="175"/>
  <rect class="accent-band" x="686" y="313" width="11" height="373"/>
  <rect class="accent-band" x="465" y="389" width="735" height="175"/>
  <rect class="accent-overlap" x="686" y="389" width="11" height="175"/>

  <text class="web-contacts" x="600" y="104" text-anchor="middle">info@dwellingowl.co.nz|www.dwellingowl.co.nz</text>

  <text class="brand-name" x="160" y="208">Dwelling</text>
  <text class="brand-name" x="160" y="299">Owl</text>

  <text class="person-name" x="851" y="447">Rhys Tane</text>
  <text class="person-role" x="851" y="488">Develover</text>

  <text class="postal-address" x="34" y="622">Street Religion Country</text>
  <text class="postal-address" x="34" y="655">PO.BOX.48215</text>

  <text class="phone-numbers" x="981" y="616">+64 21 480 2290</text>
  <text class="phone-numbers" x="981" y="649">+64 21 480 2291</text>
</svg>
</body>
</html>
```